Website design for online service business

The company provides the following services:
1 - consultancy services on existing products (like tallydesk and brisk 354)
2 - Coaching services - Coach someone on services like using/developing features with existing products, or teach how to be more productive, or improve their business using automation, etc
3 - Training
- Online training on demand on existing products via vokra (like in Tallydesk and brisk 365)
- Online courses through videos lessons and scripts by offering information products where people will need to register and pay in advance to access the online course. (productivity courses for example)

- The goal is for clients to book time with me for one of those areas without too many clicks.
- Clients will be able to Book time using an integration (it would be good to have the layout integrated with the site.) with this https://planner.brisk-suite.example/owa/calendar/BrightKelpStudio1@brightkelpstudio.bookhub.example/bookings/

- there will be areas for which i whish to build a VIP mailing list. It's referenced on the wireframes

References:
https://www.lanternfieldnotes.example/about/about-dorvan/
https://www.pebblecompass.example/
https://tallydeskguide.example/

Target Market(s)

- Small businesses
- Freelancers

Industry/Entity Type

Business

Number of Pages Required

5+ page

Font styles to use
Sans Serif

Colors

Designer to choose colors to be used in the design.

Requirements
Must have
• Must have the design optimized to the less clicks possible to achieve any action
• The colors of the site should follow the logo (provided in attach)
• It should use other color that belong to the same pallet of colors
• Should contain colors that incentivizes people to click and book something
• Images and backgrounds should be made available
• All images sizes and colors should be provided to be able to develop the site according to the design
Nice to have
• The bookings for the time should be integrated within the design. If not possible a redirection to it can work as well.
Should not have
• Links to social media
• Pop-ups
• Intrusive navigations (like navigation bares on the left or right hand side)
• Should not be a template used by many people

```html
<!DOCTYPE html>
<html lang="en">
<head>
<meta charset="utf-8">
<title>Bright Kelp Studio</title>
<link href="https://fonts.googleapis.com/css2?family=Indie+Flower&family=Open+Sans:wght@400;600;700&display=swap" rel="stylesheet">
<style>
:root{
  --brand-blue:#0b6fa4;
  --accent-orange:#f7941d;
  --sky-top:#d4effc;
  --sky-bottom:#a7ddf8;
  --ink:#333;
  --muted:#444;
  --white:#fff;
}
*{margin:0;padding:0;box-sizing:border-box}
html,body{width:800px;height:1200px;overflow:hidden;background:var(--white)}
body{font-family:"Open Sans",Verdana,sans-serif;color:var(--ink);position:relative}
.page{position:relative;width:800px;height:1200px}
.abs{position:absolute}
.btn{position:absolute;display:flex;align-items:center;justify-content:center;
  font-family:"Open Sans",sans-serif;font-weight:700;font-size:9.5px;letter-spacing:.3px;
  color:var(--white);background:var(--accent-orange);text-transform:uppercase;
  box-shadow:1px 2px 2px rgba(0,0,0,.25);text-decoration:none}
.btn--blue{background:var(--brand-blue)}
.script{font-family:"Indie Flower",cursive;font-weight:400;color:#2d2d2d;text-align:center;width:800px;left:0}

/* header */
.site-header{top:0;left:0;width:800px;height:60px;background:var(--white)}
.brand{left:100px;top:18px;display:flex;align-items:center;gap:6px;
  font-weight:700;font-size:13px;color:var(--brand-blue);letter-spacing:.5px}
.brand__dot{width:10px;height:10px;background:var(--accent-orange);border-radius:50%}
.main-nav{top:45px;left:0;font-size:9.5px;color:#333}
.main-nav a{position:absolute;white-space:nowrap;color:#333;text-decoration:none}
.main-nav a.is-active{color:var(--brand-blue)}

/* hero */
.hero{top:60px;left:0;width:800px;height:250px;
  background:radial-gradient(circle at 62% 30%,#b08a52 0%,#5e4428 30%,#2c2118 65%,#1a130e 100%)}
.hero__quote{top:150px;left:0;width:800px;text-align:center;font-family:"Indie Flower",cursive;
  font-size:33px;color:var(--white);text-shadow:0 1px 4px rgba(0,0,0,.5)}

/* help */
.help{top:310px;left:0;width:800px;height:300px;background:linear-gradient(var(--sky-top),var(--sky-bottom))}
.help__title{top:18px;font-size:25px}
.offer{position:absolute;top:71px;width:180px;text-align:center}
.offer__icon{width:51px;height:51px;border-radius:50%;background:var(--brand-blue);margin:0 auto;border:2px solid #fff}
.offer__title{margin-top:14px;font-weight:700;font-size:9.5px;letter-spacing:.4px;color:#333}
.offer__text{margin-top:12px;font-size:7.6px;line-height:12px;color:var(--muted);padding:0 14px}

/* why */
.why{top:610px;left:0;width:800px;height:266px;background:var(--white)}
.why__title{top:20px;font-size:25px}
.portrait{left:102px;top:50px;width:192px;height:192px;border-radius:50%;
  background:radial-gradient(circle at 45% 45%,#b98f78 0%,#6e6a68 45%,#3f4448 100%)}
.why__text{left:320px;top:66px;width:382px;font-size:7.8px;line-height:12px;color:var(--muted)}
.why__text p+p{margin-top:12px}

/* questions */
.questions{top:876px;left:0;width:800px;height:274px;background:linear-gradient(var(--sky-top),var(--sky-bottom))}
.questions__title{top:10px;font-size:25px}
.bubble{left:143px;top:72px;width:126px;height:118px;border-radius:50%;background:rgba(255,255,255,.25)}
.q-lines{top:59px;left:0;width:800px;text-align:center;font-size:8.8px;color:#333;line-height:12px}
.q-lines .line{display:block}
.q-lines .dots{display:block;color:var(--accent-orange);font-size:8px;letter-spacing:1px;line-height:9px}
.q-lines .lead{margin-bottom:5px}
.q-lines .reassure{font-size:15px;color:var(--brand-blue);margin:8px 0 2px;line-height:18px}
.q-lines .small{font-size:6.4px;color:#555}

/* footer */
.site-footer{top:1150px;left:0;width:800px;height:50px;background:var(--brand-blue);color:var(--white)}
.site-footer .copy{left:100px;top:20px;font-size:7.4px}
.footer-brand{left:0;width:800px;top:18px;display:flex;justify-content:center;align-items:center;gap:5px;font-size:10px;font-weight:700}
.footer-brand .brand__dot{width:8px;height:8px}
.footer-nav{right:100px;top:20px;display:flex;gap:9px;font-size:7.8px;font-weight:600}
.footer-nav a{color:var(--white);text-decoration:none}
</style>
</head>
<body>
<div class="page">

  <header class="abs site-header">
    <div class="abs brand"><span class="brand__dot"></span>BRIGHT KELP STUDIO</div>
    <nav class="abs main-nav">
      <a class="is-active" style="left:241px">HOME</a>
      <a style="left:300px">SERVICES</a>
      <a style="left:378px">BOOK ME</a>
      <a style="left:452px">BLOG</a>
      <a style="left:509px">ABOUT ME</a>
    </nav>
    <a class="btn" style="left:615px;top:34px;width:86px;height:21px">Contact me</a>
  </header>

  <section class="abs hero" role="img" aria-label="Photo of a light bulb figure plugged into a wall socket, warm dark tones">
    <p class="abs hero__quote">"...because ideas are a million"</p>
  </section>

  <section class="abs help">
    <h2 class="abs script help__title">How can I help you with your idea?</h2>

    <div class="offer" style="left:72px">
      <div class="offer__icon" role="img" aria-label="Teaching icon"></div>
      <h3 class="offer__title">I WILL TEACH YOU</h3>
      <p class="offer__text">I want to learn at my own pace. You teach me how things are done and how it works and I will do it myself.</p>
    </div>
    <div class="offer" style="left:309px">
      <div class="offer__icon" role="img" aria-label="Collaboration icon"></div>
      <h3 class="offer__title">WE DO IT TOGETHER</h3>
      <p class="offer__text">I want to learn how it works and want to do it but I need someone that works along side with me.</p>
    </div>
    <div class="offer" style="left:548px">
      <div class="offer__icon" role="img" aria-label="Done-for-you icon"></div>
      <h3 class="offer__title">I'LL DO IT FOR YOU</h3>
      <p class="offer__text">I have this great idea but I just want to have it done for me. I don't wont to do it or even learn about it.</p>
    </div>

    <a class="btn" style="left:120px;top:214px;width:86px;height:21px">Teach me</a>
    <a class="btn" style="left:357px;top:214px;width:86px;height:21px">Let's do it</a>
    <a class="btn" style="left:593px;top:214px;width:86px;height:21px">Do it for me</a>
  </section>

  <section class="abs why">
    <h2 class="abs script why__title">Why should you hire my services?</h2>
    <div class="abs portrait" role="img" aria-label="Portrait photo of the consultant outdoors"></div>
    <div class="abs why__text">
      <p>Lorem ipsum dolor sit amet, consectetur adipisicing elit, sed do eiusmod tempor incididunt ut labore et dolore magna aliqua. Ut enim ad minim veniam, quis nostrud exercitation ullamco laboris nisi ut aliquip ex ea commodo consequat. Duis aute irure dolor in reprehenderit in voluptate velit esse cillum dolore eu fugiat nulla pariatur. Excepteur sint occaecat cupidatat non proident, sunt in culpa qui officia deserunt mollit anim id est laborum. Sed ut perspiciatis unde omnis iste natus error sit voluptatem accusantium doloremque laudantium, totam rem aperiam, eaque ipsa quae ab illo inventore veritatis et quasi architecto beatae vitae dicta sunt explicabo. Nemo enim ipsam voluptatem quia voluptas sit aspernatur aut odit aut fugit, sed quia consequuntur magni dolores eos qui ratione voluptatem sequi nesciunt.</p>
      <p>Neque porro quisquam est, qui dolorem ipsum.</p>
    </div>
    <a class="btn btn--blue" style="left:320px;top:220px;width:86px;height:21px">Read more</a>
  </section>

  <section class="abs questions">
    <div class="abs bubble" role="img" aria-label="Faint speech bubble with a question mark"></div>
    <h2 class="abs script questions__title">Do you have any questions?</h2>
    <div class="abs q-lines">
      <span class="line lead">It's ok if you have questions.We haven't worked together or meath each other so how do you now if:</span>
      <span class="line">We can work together?</span>
      <span class="dots">•••</span>
      <span class="line">Understand each other?</span>
      <span class="dots">•••</span>
      <span class="line">(Did I say work together?)</span>
      <span class="dots">•••</span>
      <span class="line">I have the experience you are looking for?</span>
      <span class="line reassure">Don't worry about anything.</span>
      <span class="line">I'm here for you!</span>
      <span class="line">Use the button bellow to book a time slot where we can have a chat about what you need help with and we will take it from there.</span>
      <span class="line small">With coffee included ofcourse!</span>
    </div>
    <a class="btn" style="left:357px;top:232px;width:86px;height:21px">Book me!</a>
  </section>

  <footer class="abs site-footer">
    <p class="abs copy">Copyright @ 2018 BrightKelpStudio. All rights reserved.</p>
    <div class="abs footer-brand"><span class="brand__dot"></span>BRIGHT KELP STUDIO</div>
    <nav class="abs footer-nav">
      <a>Home</a><a>Services</a><a>Blog</a><a>About me</a><a>Contact me</a>
    </nav>
  </footer>

</div>
</body>
</html>
```